Flyer
Zielgruppe
Wir sind ein ambulanter Pflegedienst, Wir versorgen hilfebedürftige Menschen. Haben sie schon Erfahrung mit ambulanten Pflegediensten?
Aufgabenstellung
Er sollte kurz und knapp sein, nicht zu viel Text.

```html
<!DOCTYPE html>
<html lang="de">
<head>
<meta charset="utf-8">
<title>Ambulante Pflege Flyer</title>
<link href="https://fonts.googleapis.com/css2?family=Poppins:wght@300;400;500;600;700&display=swap" rel="stylesheet">
<style>
  :root {
    --red: #c11f26;
    --red-dark: #9e1419;
    --ink: #111111;
    --grey-text: #3a3a3a;
    --backdrop: #a7a8ac;
    --paper: #ffffff;
  }
  * { box-sizing: border-box; margin: 0; padding: 0; }
  html, body { width: 1200px; height: 1200px; overflow: hidden; }
  body {
    background: var(--backdrop);
    font-family: 'Poppins', sans-serif;
    color: var(--ink);
    position: relative;
  }
  .page {
    position: absolute;
    width: 537px;
    height: 686px;
    background: var(--paper);
    overflow: hidden;
  }
  /* Front page */
  .front { left: 55px; top: 104px;
    background: linear-gradient(150deg, #ffffff 0%, #f3f3f4 45%, #ffffff 70%, #f0f0f1 100%); }
  .hero-photo {
    position: absolute; left: 30px; top: 30px; width: 478px; height: 338px;
    border-radius: 16px;
    background: linear-gradient(160deg, #5b5048 0%, #a3734f 30%, #c7643a 55%, #7d4a30 75%, #3f4a32 100%);
  }
  .brand {
    position: absolute; left: 190px; top: 95px;
    display: flex; align-items: center; gap: 8px;
    color: #ffffff; font-weight: 500; font-size: 15px; letter-spacing: 0.3px;
  }
  .brand-dot { width: 12px; height: 12px; border-radius: 50%; background: var(--red); }
  .headline-band {
    position: absolute; left: 0; top: 217px; width: 346px; height: 113px;
    background: var(--red); border-radius: 0 14px 14px 0;
  }
  .headline-big {
    position: absolute; left: 37px; top: 222px;
    color: #fff; font-weight: 700; font-size: 60px; line-height: 1; letter-spacing: 1px;
  }
  .headline-big .outline { color: transparent; -webkit-text-stroke: 2px #fff; font-weight: 600; }
  .headline-small {
    position: absolute; left: 38px; top: 284px;
    color: #fff; font-weight: 300; font-size: 33px; line-height: 1;
  }
  .address {
    position: absolute; left: 60px; top: 415px; width: 420px; text-align: center;
    font-size: 13.5px; color: var(--grey-text); line-height: 1.3;
  }
  .address svg { vertical-align: -2px; margin-right: 4px; }
  .contact-box {
    position: absolute; left: 30px; top: 479px; width: 478px; height: 52px;
    border: 2px solid var(--red); border-radius: 8px;
    display: flex; align-items: center;
  }
  .contact { flex: 1; display: flex; gap: 8px; padding-left: 38px; }
  .contact + .contact { border-left: 2px solid #bbb; padding-left: 28px; }
  .contact-name { color: var(--red); font-weight: 700; font-size: 12.5px; line-height: 1.2; }
  .contact-phone { font-size: 12.5px; color: var(--grey-text); line-height: 1.2; }
  .contact svg { margin-top: 2px; }
  .email {
    position: absolute; left: 0; width: 100%; top: 564px; text-align: center;
    font-size: 13.5px; color: var(--grey-text);
  }
  .email svg { vertical-align: -3px; margin-right: 8px; }
  .hours { position: absolute; left: 0; width: 100%; top: 610px; text-align: center; font-size: 13px; color: var(--grey-text); line-height: 1.2; }
  .hours-label { color: var(--red); font-weight: 700; }

  /* Back page */
  .back { left: 607px; top: 410px; }
  .services-title { position: absolute; left: 31px; top: 26px; font-weight: 700; font-size: 23px; line-height: 1.02; }
  .services-title .accent { color: var(--red); }
  .title-rule { position: absolute; left: 30px; top: 82px; width: 175px; height: 2px; background: var(--red); }
  .care-photo {
    position: absolute; left: 299px; top: 28px; width: 238px; height: 246px;
    border-radius: 120px 0 0 40px;
    background: linear-gradient(135deg, #e9e3dc 0%, #c9b8a6 40%, #9a7559 70%, #ffffff 100%);
  }
  .basic-care { position: absolute; left: 35px; top: 100px; width: 240px; }
  .section-label { color: var(--red); font-weight: 700; font-size: 12.5px; margin-bottom: 4px; }
  .bullets { list-style: none; font-size: 10.2px; font-weight: 500; line-height: 1.2; }
  .bullets li { position: relative; padding-left: 7px; margin-bottom: 5px; }
  .bullets li::before { content: "•"; position: absolute; left: 0; color: var(--red); }
  .treatment-box {
    position: absolute; left: 15px; top: 301px; width: 507px; height: 232px;
    background: linear-gradient(135deg, var(--red) 0%, #b51c22 50%, var(--red-dark) 100%);
    border-radius: 14px; color: #fff; padding: 16px 15px;
  }
  .treatment-title { font-weight: 700; font-size: 16.5px; line-height: 1.1; }
  .treatment-intro { font-size: 10.5px; font-weight: 500; margin-top: 6px; }
  .treatment-cols { display: flex; gap: 20px; margin-top: 14px; }
  .treatment-cols ul { list-style: none; font-size: 9.8px; line-height: 1.15; }
  .treatment-cols ul:first-child { width: 262px; }
  .treatment-cols li { position: relative; padding-left: 7px; margin-bottom: 5.5px; }
  .treatment-cols li::before { content: "•"; position: absolute; left: 0; }
  .relief-title { position: absolute; left: 30px; top: 548px; font-weight: 600; font-size: 16.5px; }
  .relief-rule { position: absolute; left: 30px; top: 576px; width: 192px; height: 2px; background: var(--red); }
  .relief-price { position: absolute; left: 30px; top: 586px; font-weight: 700; font-size: 19.5px; line-height: 1.18; }
  .relief-price .accent { color: var(--red); }
  .relief-list { position: absolute; left: 305px; top: 587px; list-style: none; font-size: 13.5px; line-height: 1.36; }
  .relief-list li { position: relative; padding-left: 8px; }
  .relief-list li::before { content: "•"; position: absolute; left: 0; color: var(--red); }
</style>
</head>
<body>

<section class="page front">
  <div class="hero-photo" role="img" aria-label="Luftaufnahme einer Kleinstadt mit roten Dächern"></div>
  <div class="brand"><span class="brand-dot"></span>Lindner &amp; Hofer Ambulante Pflege</div>
  <div class="headline-band"></div>
  <div class="headline-big">24 <span class="outline">HOUR</span></div>
  <div class="headline-small">ON-CALL SERVICE</div>

  <p class="address">
    <svg width="10" height="13" viewBox="0 0 10 13"><path d="M5 0C2.2 0 0 2.2 0 5c0 3.5 5 8 5 8s5-4.5 5-8c0-2.8-2.2-5-5-5zm0 7a2 2 0 110-4 2 2 0 010 4z" fill="#c11f26"/></svg>Outpatient care Lindner &amp; Hofer Am Lindenhof 12<br>84000 Lindenfeld
  </p>

  <div class="contact-box">
    <div class="contact">
      <svg width="13" height="13" viewBox="0 0 24 24"><path d="M6.6 10.8a15 15 0 006.6 6.6l2.2-2.2c.3-.3.7-.4 1-.2 1.1.4 2.3.6 3.6.6.6 0 1 .4 1 1V20c0 .6-.4 1-1 1A17 17 0 013 4c0-.6.4-1 1-1h3.5c.6 0 1 .4 1 1 0 1.3.2 2.5.6 3.6.1.3 0 .7-.2 1z" fill="#c11f26"/></svg>
      <div><div class="contact-name">MS. TOMI VEKNER</div><div class="contact-phone">01701234567</div></div>
    </div>
    <div class="contact">
      <svg width="13" height="13" viewBox="0 0 24 24"><path d="M6.6 10.8a15 15 0 006.6 6.6l2.2-2.2c.3-.3.7-.4 1-.2 1.1.4 2.3.6 3.6.6.6 0 1 .4 1 1V20c0 .6-.4 1-1 1A17 17 0 013 4c0-.6.4-1 1-1h3.5c.6 0 1 .4 1 1 0 1.3.2 2.5.6 3.6.1.3 0 .7-.2 1z" fill="#c11f26"/></svg>
      <div><div class="contact-name">MR. MORITZ HOFER</div><div class="contact-phone">015209876543</div></div>
    </div>
  </div>

  <p class="email">
    <svg width="19" height="12" viewBox="0 0 19 12"><rect width="19" height="12" fill="#c11f26"/><path d="M0 0l9.5 7L19 0" stroke="#fff" stroke-width="1.2" fill="none"/></svg>info@pflege-lindenhof.de
  </p>

  <p class="hours"><span class="hours-label">OFFICE HOURS:</span><br>Mon-Fri 8:00 a.m. - 4:00 p.m</p>
</section>

<section class="page back">
  <h1 class="services-title"><span class="accent">UNSERE</span><br>LEISTUNGEN</h1>
  <div class="title-rule"></div>
  <div class="care-photo" role="img" aria-label="Foto einer Pflegerin mit einer älteren Dame"></div>

  <div class="basic-care">
    <h2 class="section-label">Grundpflege nach SGB XI:</h2>
    <ul class="bullets">
      <li>Körperpflege, Duschen, Waschen, Baden, Hautpflege Hilfe beim An- und Auskleiden</li>
      <li>Mundpflege Rasieren, Kämmen Haar-und Nagelpflege</li>
      <li>Hilfe bei der Nahrungsaufnahme</li>
      <li>Verabreichung von Sondennahrung</li>
      <li>Stoma Pflege</li>
      <li>Inkontinenzversorgung</li>
      <li>Lagern</li>
      <li>Mobilisieren</li>
    </ul>
  </div>

  <div class="treatment-box">
    <h2 class="treatment-title">Behandlungspflege nach SGB V:</h2>
    <p class="treatment-intro">Nach ärztlicher Anordnung bieten wir folgende Leistungen:</p>
    <div class="treatment-cols">
      <ul>
        <li>Moderne Wundversorgung akute<br>und chronische Wunden</li>
        <li>Dekubitus Behandlung</li>
        <li>Injektionen und Infusionen</li>
        <li>Blutzucker Messung Blutdruck und Puls Messung</li>
        <li>PEG und PUFI-Versorgung</li>
        <li>Schmerztherapie mit Schmerzpumpe</li>
        <li>Medikamentenbox richten</li>
        <li>Medikamente verabreichen</li>
      </ul>
      <ul>
        <li>Kompressionstherapie -Stomaversorgung Zusatzleistungen</li>
        <li>Hauswirtschaftliche Versorgung</li>
        <li>Hausnotruf durch Kooperationspartner</li>
        <li>Verhinderungspflege und Entlastung der Angehörigen</li>
        <li>Essen auf Rädern</li>
        <li>24 Stunden Rufbereitschaft</li>
        <li>Beratungseinsätze nach <b>§ 37 Abs. 3 SGB XI</b> (Bei Bezug von Pflegegeld)</li>
      </ul>
    </div>
  </div>

  <h2 class="relief-title">Entlastungsleistungen</h2>
  <div class="relief-rule"></div>
  <p class="relief-price">Die Leistung beträgt<br>pauschal <span class="accent">125€ im Monat<br>für Pflegegrad 1-5</span></p>
  <ul class="relief-list">
    <li>Spaziergänge</li>
    <li>Beschäftigung</li>
    <li>Hauswirtschaftliche Leistungen</li>
    <li>Betreuungsmaßnahmen</li>
  </ul>
</section>

</body>
</html>
```